San Francisco Pet Care Non Profit

Business Card Design for non profit organization.
We are a mobile pet care team who supports and attends to pets whose owners are homeless. Thanks for your help and creativity.

Industry/Entity Type

Non Profit

Contact Information for Business Card

Marisol Keddy
President
2871 Larkmoor Street, #512
San Francisco, CA 94187
phone: 415-729-3846
fax: 415-781-4052
marisol@tidywagonvan.org
website: tidywagonvan.org
facebook: pawfeed.com/TidyWagonVan

Font styles to use
Serif
Sans Serif

Colors

Designer to choose colors to be used in the design.

Requirements
Must have
• above details and attached logo

```html
<!DOCTYPE html>
<html lang="en">
<head>
<meta charset="utf-8">
<title>TidyWagonVan Business Card</title>
<link href="https://fonts.googleapis.com/css2?family=Oswald:wght@500&family=Work+Sans:wght@400;600&display=swap" rel="stylesheet">
<style>
  :root {
    --backdrop: #262626;
    --card: #1b1b1b;
    --card-edge: #2c2c2c;
    --accent: #1ba3e0;
    --text-light: #f2f2f2;
    --text-muted: #bdbdbd;
    --brand-grey: #9a9a9a;
    --tagline-grey: #6f6f6f;
  }
  * { margin: 0; padding: 0; box-sizing: border-box; }
  html, body {
    width: 1200px; height: 900px; overflow: hidden;
    background: var(--backdrop);
  }
  .canvas {
    position: relative; width: 1200px; height: 900px;
    display: flex; flex-direction: column; align-items: center;
    justify-content: center; gap: 40px;
  }
  .card {
    position: relative; width: 700px; height: 380px; overflow: hidden;
    background: linear-gradient(135deg, #161616 0%, var(--card) 60%, #222 100%);
    border: 1px solid var(--card-edge);
    box-shadow: 0 14px 30px rgba(0,0,0,0.45);
    font-family: "Work Sans", sans-serif;
    color: var(--text-light);
  }

  /* Front */
  .brand {
    position: absolute; left: 0; right: 0; top: 140px;
    display: flex; flex-direction: column; align-items: center;
  }
  .brand-row { display: flex; align-items: center; gap: 18px; }
  .brand-dot {
    width: 54px; height: 54px; border-radius: 50%;
    background: var(--brand-grey);
  }
  .brand-name {
    font-weight: 600; font-size: 46px;
    color: var(--brand-grey); letter-spacing: 0.5px;
  }
  .brand-tagline {
    margin-top: 4px; margin-left: 72px;
    font-size: 18px; font-weight: 600; color: var(--tagline-grey); letter-spacing: 0.5px;
  }

  /* Back */
  .person {
    position: absolute; right: 416px; top: 130px; text-align: right;
  }
  .person-name {
    font-family: "Oswald", sans-serif; font-weight: 500;
    font-size: 37px; line-height: 1; color: var(--accent); letter-spacing: 1px;
    white-space: nowrap;
  }
  .person-title {
    margin-top: 6px; font-size: 18px; color: var(--text-muted); letter-spacing: 1px;
  }
  .divider {
    position: absolute; left: 300px; top: 110px;
    width: 3px; height: 100px; background: var(--accent);
  }
  .contacts {
    position: absolute; left: 325px; top: 108px; list-style: none;
  }
  .contacts li {
    display: flex; align-items: center; gap: 10px;
    font-size: 17px; line-height: 21px; letter-spacing: 0.8px;
    white-space: nowrap;
  }
  .contacts svg { width: 12px; height: 12px; flex: none; }
  .contacts .highlight { color: var(--accent); }
  .address {
    position: absolute; left: 70px; top: 300px;
    font-size: 18px; letter-spacing: 1px; color: var(--text-light);
    white-space: nowrap;
  }
</style>
</head>
<body>
<main class="canvas">
  <section class="card card-front">
    <div class="brand">
      <div class="brand-row">
        <span class="brand-dot"></span>
        <span class="brand-name">TidyWagonVan</span>
      </div>
      <span class="brand-tagline">Mobile Pet Care Team</span>
    </div>
  </section>

  <section class="card card-back">
    <div class="person">
      <h1 class="person-name">MARISOL KEDDY</h1>
      <p class="person-title">President</p>
    </div>
    <div class="divider"></div>
    <ul class="contacts">
      <li>
        <svg viewBox="0 0 12 12"><path d="M2.5 1l2 2.2-1 1.3a7 7 0 0 0 4 4l1.3-1 2.2 2-1 1.5C6 11 1 6 1 2.5z" fill="#1ba3e0"/></svg>
        415-729-3846
      </li>
      <li>
        <svg viewBox="0 0 12 12"><rect x="3" y="1" width="6" height="3" fill="#1ba3e0"/><rect x="1" y="4.5" width="10" height="4.5" rx="1" fill="#1ba3e0"/><rect x="3" y="8" width="6" height="3" fill="#1ba3e0"/></svg>
        415-781-4052
      </li>
      <li>
        <svg viewBox="0 0 12 12"><rect x="1" y="2.5" width="10" height="7" fill="none" stroke="#1ba3e0" stroke-width="1.2"/><path d="M1 2.5l5 4 5-4" fill="none" stroke="#1ba3e0" stroke-width="1.2"/></svg>
        marisol@tidywagonvan.org
      </li>
      <li>
        <svg viewBox="0 0 12 12"><circle cx="6" cy="6" r="5" fill="none" stroke="#1ba3e0" stroke-width="1.2"/><ellipse cx="6" cy="6" rx="2" ry="5" fill="none" stroke="#1ba3e0" stroke-width="1"/><path d="M1 6h10" stroke="#1ba3e0" stroke-width="1"/></svg>
        <span>www.<span class="highlight">tidywagonvan</span>.org</span>
      </li>
      <li>
        <svg viewBox="0 0 12 12"><rect x="2" y="2" width="8" height="8" fill="#1ba3e0"/></svg>
        pawfeed.com/TidyWagonVan
      </li>
    </ul>
    <p class="address">2871 Larkmoor Street, #512 San Francisco, CA 94187</p>
  </section>
</main>
</body>
</html>
```